Brightfield Optics seeks updated contemporary business card

Brightfield Optics utilizes advanced technology and we take pride in the modern look and feel of our practice. We like our current card, but it's been four years so it is time for an update.

Target Market(s)

Females 25-45 make the most health care decisions for their family.

Contact Information for Business Card

Clean front. Back with info and with empty space for appointment time or other small note

Requirements
Must have
• Logo
Ridge Marketvale, 28413 E Larkspur Ave
Cedar Terrace Marketvale, 4638 S Dunmore Rd
Call or text: 509-342-1968
email: hello@brightfieldoptics.example
brightfieldoptics.example
Dr Tobias Werring & Associates

```html
<!DOCTYPE html>
<html lang="en">
<head>
<meta charset="utf-8">
<title>Brightfield Optics — Business Card</title>
<link rel="stylesheet" href="https://fonts.googleapis.com/css2?family=Poppins:wght@400;600;700&display=swap">
<style>
  :root {
    --navy: #3a5380;
    --navy-text: #2f4c7e;
    --accent: #1a8fd0;
    --accent-light: #29aee6;
    --ink: #4a4f5a;
    --paper: #ffffff;
    --backdrop: #e9ebef;
  }
  * { box-sizing: border-box; margin: 0; padding: 0; }
  html, body { width: 1200px; height: 1189px; overflow: hidden; }
  body {
    background: var(--backdrop);
    font-family: "Poppins", sans-serif;
    display: flex;
    flex-direction: column;
    align-items: center;
    justify-content: center;
    gap: 56px;
  }
  .card {
    width: 900px;
    height: 514px;
    border-radius: 32px;
    position: relative;
    box-shadow: 0 14px 34px rgba(0,0,0,0.18);
    overflow: hidden;
  }
  .card-front {
    background: var(--navy);
    display: flex;
    align-items: center;
    justify-content: center;
    gap: 22px;
  }
  .brand-dot {
    width: 44px; height: 44px;
    border-radius: 50%;
    background: var(--paper);
  }
  .brand-name-front {
    color: var(--paper);
    font-weight: 700;
    font-size: 60px;
    letter-spacing: 1px;
    text-transform: uppercase;
  }
  .card-back { background: var(--paper); }
  .back-brand {
    position: absolute;
    top: 92px; right: 70px;
    display: flex; align-items: center; gap: 16px;
  }
  .back-brand .brand-dot { background: var(--accent-light); width: 34px; height: 34px; }
  .brand-name-back {
    color: var(--navy-text);
    font-weight: 700;
    font-size: 40px;
    text-transform: uppercase;
    letter-spacing: 0.5px;
  }
  .divider {
    position: absolute;
    height: 2px;
    background: var(--accent);
  }
  .divider-top { top: 232px; left: 470px; right: 60px; }
  .divider-name { top: 318px; left: 60px; width: 400px; }
  .practitioner {
    position: absolute;
    top: 256px; left: 60px;
    color: var(--navy-text);
    font-weight: 700;
    font-size: 34px;
  }
  .contact-list {
    position: absolute;
    top: 344px; left: 60px;
    list-style: none;
    display: flex; flex-direction: column; gap: 10px;
  }
  .contact-item {
    display: flex; align-items: center; gap: 16px;
    color: var(--ink);
    font-size: 22px;
  }
  .contact-icon { width: 30px; height: 30px; flex: none; }
  .locations {
    position: absolute;
    top: 300px; right: 60px;
    color: var(--ink);
    font-size: 19px;
    line-height: 1.7;
    text-align: right;
    list-style: none;
  }
</style>
</head>
<body>

<section class="card card-front" aria-label="Card front">
  <span class="brand-dot"></span>
  <span class="brand-name-front">Brightfield Optics</span>
</section>

<section class="card card-back" aria-label="Card back">
  <div class="back-brand">
    <span class="brand-dot"></span>
    <span class="brand-name-back">Brightfield Optics</span>
  </div>
  <div class="divider divider-top"></div>

  <h1 class="practitioner">Dr Tobias Werring &amp; Associates</h1>
  <div class="divider divider-name"></div>

  <ul class="contact-list">
    <li class="contact-item">
      <svg class="contact-icon" viewBox="0 0 30 30"><circle cx="15" cy="15" r="14" fill="#29aee6"/><path d="M10.5 8.5l3 3-1.6 1.8c.9 1.9 2.2 3.2 4 4l1.8-1.6 3 3-1.6 2c-4.8-.6-9.2-5-9.8-9.8z" fill="#fff"/></svg>
      <span>509-342-1968</span>
    </li>
    <li class="contact-item">
      <svg class="contact-icon" viewBox="0 0 30 30"><circle cx="15" cy="15" r="14" fill="#29aee6"/><rect x="8" y="10" width="14" height="10" rx="1" fill="#fff"/><path d="M8.5 10.5l6.5 5 6.5-5" stroke="#29aee6" stroke-width="1.4" fill="none"/></svg>
      <span>hello@brightfieldoptics.example</span>
    </li>
    <li class="contact-item">
      <svg class="contact-icon" viewBox="0 0 30 30"><circle cx="15" cy="15" r="14" fill="#29aee6"/><g stroke="#fff" stroke-width="1.4" fill="none"><circle cx="15" cy="15" r="7"/><ellipse cx="15" cy="15" rx="3" ry="7"/><path d="M8 15h14"/></g></svg>
      <span>brightfieldoptics.example</span>
    </li>
  </ul>

  <ul class="locations">
    <li>Ridge Marketvale, 28413 E Larkspur Ave</li>
    <li>Cedar Terrace Marketvale, 4638 S Dunmore Rd</li>
  </ul>
</section>

</body>
</html>
```